Popup Nightclub Grand Opening Flyer

We need to design a flyer for the grand opening of an upscale, exclusive nightclub called "Lanternfall". The design needs to be chic and exclusive. The background should be black and the text should primarily be white. We like minimalist designs.

Here is the text for the flyer
-
Velvetrope Atlanta Presents

Lanternfall (LOGO)

A Popup Nightclub Experience
For one night Only

Friday, October 18, 2013
Party begins at 9PM

INVITE ONLY

See invitation for location details
(Velvetrope Atlanta logo)

-
Examples we like

http://cdn2-b.brivelpost.com/sites/default/files/styles/image_content_width/hash/3d/fa/1472093815_4471_flyer.jpg?itok=R8kqWm2z

http://api.plovra.com/files/7Kqq-Tr82XXB3pQzJvmtR5HL2W719E4nbRtC6KLd4HsfM8Y2qTDK-VmjwDoNqLX4QBzTHD9nakRbVx3m-Pfq8htc3MDTWr5p4/2zelSaturdays.jpg

http://quenmar.com/wp-content/uploads/yootheme/widgetkit/gallery/2zel/2zel-gen_vroom4-01.jpg

Hi All, one thing that we are seeing that we don't like is on over emphasis on the phrase "a popup nightclub experience" please don't make this the largest thing on the flyer

Target Market(s)

Target market is 25-35 year olds who are affluent (rich) and like luxury brands

Requirements
Must have
• Dark Background
Nice to have
• Velvetrope Logo on the bottom
Modern text that isn't curvy
Should not have
• Curved text

```html
<!DOCTYPE html>
<html lang="en">
<head>
<meta charset="utf-8">
<title>Lanternfall Popup Nightclub – Flyer</title>
<link href="https://fonts.googleapis.com/css2?family=Lato:wght@700&family=Josefin+Sans:wght@300&family=Poiret+One&display=swap" rel="stylesheet">
<style>
  :root {
    --ink: #000000;
    --white: #ffffff;
    --deco: #b9e4e1;
    --deco-glow: rgba(90, 210, 190, 0.35);
    --nebula: #2f8c7c;
    --nebula-soft: #15443c;
    --nebula-pink: #b36ac4;
    --silver: #c4c4c6;
  }
  * { margin: 0; padding: 0; box-sizing: border-box; }
  html, body { width: 928px; height: 1200px; overflow: hidden; background: var(--ink); }
  .flyer {
    position: relative;
    width: 928px;
    height: 1200px;
    overflow: hidden;
    background: var(--ink);
  }
  .nebula-backdrop {
    position: absolute;
    inset: 0;
    background:
      radial-gradient(ellipse 220px 140px at 170px 250px, rgba(80,200,170,0.55), transparent 70%),
      radial-gradient(ellipse 380px 260px at 260px 420px, rgba(47,140,124,0.45), transparent 70%),
      radial-gradient(ellipse 300px 420px at 520px 700px, rgba(40,120,105,0.40), transparent 72%),
      radial-gradient(ellipse 260px 200px at 820px 260px, rgba(30,95,85,0.35), transparent 70%),
      radial-gradient(circle 20px at 330px 200px, rgba(179,106,196,0.7), transparent 70%),
      radial-gradient(circle 18px at 335px 465px, rgba(179,106,196,0.6), transparent 70%),
      linear-gradient(160deg, #0a1f1c 0%, #061210 45%, #020605 100%);
  }
  .presenter {
    position: absolute;
    top: 12px; left: 0; right: 0;
    text-align: center;
    font-family: "Lato", sans-serif;
    font-weight: 700;
    font-size: 44px;
    color: var(--white);
  }
  .deco {
    font-family: "Poiret One", sans-serif;
    color: var(--deco);
    text-transform: uppercase;
    text-shadow: 0 0 8px var(--deco-glow);
  }
  .invite-only {
    position: absolute;
    top: 142px; left: 0; right: 0;
    display: flex;
    justify-content: center;
    gap: 72px;
    font-size: 38px;
    letter-spacing: 3px;
  }
  .brand-mark {
    position: absolute;
    left: 334px; top: 196px;
    width: 260px; height: 260px;
    border-radius: 50%;
    background: var(--silver);
  }
  .brand-name {
    position: absolute;
    top: 530px; left: 0; right: 0;
    text-align: center;
    font-family: "Josefin Sans", sans-serif;
    font-weight: 300;
    font-size: 92px;
    letter-spacing: 8px;
    color: var(--white);
    text-transform: uppercase;
  }
  .details {
    position: absolute;
    left: 0; right: 0;
    text-align: center;
  }
  .date { top: 752px; font-size: 60px; letter-spacing: 2px; }
  .start { top: 848px; font-size: 46px; letter-spacing: 2px; }
  .concept { top: 928px; font-size: 46px; letter-spacing: 2px; }
  .one-night { top: 1002px; font-size: 46px; letter-spacing: 2px; }
  .footer {
    position: absolute;
    left: 22px; right: 22px; top: 1118px;
    display: flex;
    justify-content: space-between;
    align-items: center;
  }
  .location-note { font-size: 32px; letter-spacing: 1px; }
  .host-name {
    font-family: "Josefin Sans", sans-serif;
    font-weight: 300;
    font-size: 34px;
    color: var(--white);
  }
</style>
</head>
<body>
  <main class="flyer">
    <div class="nebula-backdrop" role="img" aria-label="Deep space nebula in teal and green tones with faint violet stars"></div>

    <h1 class="presenter">Velvetrope Atlanta Presents</h1>

    <div class="invite-only deco"><span>Invite</span><span>Only</span></div>

    <div class="brand-mark" aria-hidden="true"></div>
    <h2 class="brand-name">Lanternfall</h2>

    <p class="details deco date">Friday, October 18, 2013</p>
    <p class="details deco start">Party begins at 9PM</p>
    <p class="details deco concept">A Popup Nightclub Experience</p>
    <p class="details deco one-night">For One Night Only</p>

    <footer class="footer">
      <span class="deco location-note">See invitation for location details</span>
      <span class="host-name">Velvetrope</span>
    </footer>
  </main>
</body>
</html>
```